Report presentation for measurement or inline reports

First page of report. Our inline reporting will come in a maintenance map. We want a modern first page and a real eye-catcher for a new company based in the Netherlands called: RTP Luchtregeling B.V. We are a service company witch measures, balances and give advices at indoor climate HVAC installations. We would like to see designs that use the color blue. We deliver our services to different buildings: Hospitals, atractions, officebuildings, government buildings, swimming pools and schools. Our website: www.rtpl.nl
Updates

Can you all add the new logo please. The companyname is RTP Luchtregeling B.V.. In witch format can i retrieve the design?

Industry/Entity Type

It Company

Colors
0255a3
3176b5
85abd2
cedeed
eaf1f7
ffffff

Requirements
Must have
• Projectname; projectplace; Inline or measure report; date; logo; companyname. it must be easy printable so not to much colours.
• The companyname is: RTP Luchtregeling B.V.. Please add the name. A new logo is updated.
Nice to have
• Maybe some pictures from hvac installations, buildings or measure

```html
<!DOCTYPE html>
<html lang="nl">
<head>
<meta charset="utf-8">
<title>Inline reporting – RTP Luchtregeling B.V.</title>
<link href="https://fonts.googleapis.com/css2?family=Poppins:wght@400;500&display=swap" rel="stylesheet">
<style>
  :root {
    --blue-deep: #0255a3;
    --blue-mid: #3176b5;
    --blue-soft: #85abd2;
    --blue-pale: #cedeed;
    --blue-mist: #eaf1f7;
    --white: #ffffff;
    --ink: #3a3f47;
    --rule: #b9bec5;
    --backdrop: #e6eaee;
  }
  * { box-sizing: border-box; margin: 0; padding: 0; }
  html, body { width: 1200px; height: 797px; overflow: hidden; }
  body {
    background: var(--backdrop);
    font-family: "Poppins", sans-serif;
    color: var(--ink);
    position: relative;
  }
  .report-cover {
    position: absolute;
    left: 330px; top: 16px;
    width: 540px; height: 764px;
    background: linear-gradient(180deg, var(--white) 0%, #f4f5f7 100%);
    box-shadow: 0 6px 24px rgba(20, 40, 70, .18);
  }
  .cover-title {
    position: absolute; left: 170px; top: 62px;
    font-size: 40px; font-weight: 400; color: var(--blue-deep);
    letter-spacing: .2px;
  }
  .tile { position: absolute; border-radius: 12px; }
  .photo { border-radius: 20px; }
  .photo-building {
    left: 110px; top: 150px; width: 262px; height: 126px;
    background: linear-gradient(135deg, #4e6a94 0%, #a7b6cc 45%, #d8c38a 75%, #5d6b5a 100%);
  }
  .photo-hospital {
    left: 240px; top: 290px; width: 216px; height: 152px;
    background: linear-gradient(180deg, #6f8a94 0%, #b9c7c9 45%, #9aa3a0 70%, #6f8c63 100%);
  }
  .tile-accent { left: 386px; top: 204px; width: 48px; height: 48px; background: var(--blue-mid); border-radius: 9px; }
  .tile-large  { left: 116px; top: 290px; width: 114px; height: 114px; background: var(--blue-deep); border-radius: 14px; }
  .tile-tiny   { left: 82px;  top: 382px; width: 28px;  height: 28px;  background: var(--blue-deep); border-radius: 6px; }
  .tile-medium { left: 120px; top: 414px; width: 74px;  height: 74px;  background: #1a62ad; border-radius: 12px; }

  .project {
    position: absolute; left: 78px; top: 512px;
  }
  .project-name { font-size: 23px; font-weight: 500; color: var(--blue-deep); line-height: 1.15; }
  .project-scope { font-size: 15px; color: var(--blue-mid); margin-top: 2px; }
  .project-meta { display: flex; gap: 22px; margin-top: 14px; font-size: 15px; line-height: 1.25; }
  .meta-divider { width: 2px; background: var(--blue-mid); margin-top: 14px; height: 34px; }
  .meta-item:last-child { padding-top: 18px; }

  .company {
    position: absolute; left: 78px; top: 648px;
  }
  .company-name {
    display: flex; align-items: center; gap: 8px;
    font-size: 20px; font-weight: 500; color: var(--blue-deep);
  }
  .company-name::before {
    content: ""; width: 22px; height: 22px; background: var(--blue-deep); border-radius: 4px;
  }
  .company-address { font-size: 11px; margin-top: 4px; }

  .footer-rule { position: absolute; left: 30px; right: 30px; top: 716px; height: 1px; background: var(--rule); }
  .contact-row {
    position: absolute; left: 60px; right: 60px; top: 726px;
    display: flex; justify-content: space-between; font-size: 8.5px;
  }
  .cert-badge {
    position: absolute; right: 36px; top: 672px; width: 36px; height: 36px;
    border-radius: 50%; border: 2px solid var(--ink);
  }
</style>
</head>
<body>
  <main class="report-cover">
    <h1 class="cover-title">Inline reporting</h1>

    <div class="tile photo photo-building" role="img" aria-label="Foto van een modern kantoorgebouw met glazen gevel in de avond"></div>
    <div class="tile tile-accent"></div>
    <div class="tile tile-large"></div>
    <div class="tile photo photo-hospital" role="img" aria-label="Luchtimpressie van een ziekenhuiscomplex met hoge toren"></div>
    <div class="tile tile-tiny"></div>
    <div class="tile tile-medium"></div>

    <section class="project">
      <h2 class="project-name">ROC Westerpoort Definitief</h2>
      <p class="project-scope">Lucht en waterzijdig inregelen</p>
      <div class="project-meta">
        <p class="meta-item">Projectnummer<br>MI11397</p>
        <span class="meta-divider"></span>
        <p class="meta-item">Rapportdatum<br>3-10-2011</p>
      </div>
    </section>

    <section class="company">
      <p class="company-name">RTP Luchtregeling B.V.</p>
      <p class="company-address">Postbus 482 5261 KL Vught</p>
    </section>

    <div class="cert-badge" aria-hidden="true"></div>
    <div class="footer-rule"></div>
    <footer class="contact-row">
      <span>Tel: +31 (0) 73 512 4680</span>
      <span>Fax: +31 (0) 73 512 4689</span>
      <span>Mobiel: +31 (0) 6 204 719 35</span>
      <span>E-mail: info@rtpl.nl</span>
    </footer>
  </main>
</body>
</html>
```